Morden, Creative, Unique, Independent Wine Shop

1. We are a brand new wine shop located in Melbourne Australia, we have our logo already, simply use the logo to design a business card.
2. I have uploaded our logo in two versions, with or without shadow, any of them is acceptable.
3. Make it as creative and unique as possible, no limitation of shape, color combination, geometry pattern, fonts, composing etc.
3. Info on the card:
- Brambleford Wine Cellar (Not very necessary if logo is obviously shown)
- 42 Ferncastle Steet, Hampton, Victoria, Australia 3188
- +61 3 9018 4637
- www.bramblefordwinecellar.com.au
- bramblefordwinecellar@mailvista.com
- Additional icons: Google, Instagram, Facebook, Twitter
4. Once again, forget it is a commercial card, make it special.

```html
<!DOCTYPE html>
<html lang="en">
<head>
<meta charset="utf-8">
<title>Brambleford Wine Cellar – Business Card</title>
<link rel="stylesheet" href="https://fonts.googleapis.com/css2?family=Lato:wght@400;700&display=swap">
<style>
  :root {
    --backdrop: #7d3b3e;
    --card: #ffffff;
    --ink: #1f2430;
    --wine: #b3203f;
    --wine-deep: #8e1a34;
    --graphite: #5b5b5e;
    --mist: #ececee;
    --shadow: rgba(0, 0, 0, 0.4);
  }
  * { box-sizing: border-box; margin: 0; padding: 0; }
  html, body {
    width: 1200px; height: 960px; overflow: hidden;
    background: var(--backdrop);
    font-family: "Lato", sans-serif;
    color: var(--ink);
  }
  .canvas { position: relative; width: 1200px; height: 960px; }
  .card {
    position: absolute;
    background: var(--card);
    box-shadow: 3px 4px 6px var(--shadow);
  }

  /* Back side: contact details */
  .card-back { left: 70px; top: 330px; width: 552px; height: 340px; }
  .address {
    position: absolute; left: 42px; top: 86px;
    font-size: 14px; line-height: 23px;
  }
  .contact-list {
    position: absolute; left: 42px; top: 216px;
    list-style: none; font-size: 11px; line-height: 19px;
  }
  .contact-list li { display: flex; align-items: center; gap: 8px; }
  .contact-list svg { width: 10px; height: 10px; flex: none; }
  .back-mark {
    position: absolute; right: 40px; top: 90px; width: 100px;
    display: flex; flex-direction: column; align-items: center; gap: 8px;
  }
  .back-mark .mark-dot {
    width: 34px; height: 34px; border-radius: 50%; background: var(--graphite);
  }
  .back-mark p {
    text-align: center; font-size: 11px; font-weight: 700;
    line-height: 14px; color: var(--wine);
  }

  /* Front side: brand */
  .card-front { left: 700px; top: 190px; width: 346px; height: 560px; }
  .brand-name {
    position: absolute; left: 0; right: 0; top: 78px;
    text-align: center; font-size: 28px; font-weight: 700;
    line-height: 30px; color: var(--wine); letter-spacing: 1px;
  }
  .brand-name small {
    display: block; font-size: 13px; letter-spacing: 4px;
    text-transform: uppercase; line-height: 22px;
  }
  .social-row {
    position: absolute; left: 0; right: 0; top: 160px;
    display: flex; justify-content: center; gap: 10px;
  }
  .social-row span {
    width: 13px; height: 13px; border-radius: 2px; background: var(--wine-deep);
  }
  .emblem {
    position: absolute; left: 58px; top: 214px; width: 230px; height: 230px;
    border-radius: 50%;
    background: radial-gradient(circle at 40% 35%, var(--mist) 0%, #b9b9bc 55%, var(--graphite) 100%);
    box-shadow: inset 2px 3px 6px rgba(0,0,0,0.25);
  }
  .emblem-caption {
    position: absolute; left: 0; right: 0; top: 474px;
    text-align: center; font-size: 11px; letter-spacing: 3px;
    text-transform: uppercase; color: var(--graphite);
  }
</style>
</head>
<body>
<main class="canvas">
  <section class="card card-back" aria-label="Card back with contact details">
    <p class="address">42 Ferncastle Steet, Hampton<br>Victoria, Australia 3188</p>
    <ul class="contact-list">
      <li>
        <svg viewBox="0 0 10 10" aria-hidden="true"><path d="M1 3 Q5 0 9 3 L8 4.5 L6.5 3.8 L6.5 3 Q5 2.6 3.5 3 L3.5 3.8 L2 4.5 Z M2.5 5 H7.5 L8.5 9 H1.5 Z" fill="var(--wine)"/></svg>
        +61 3 9018 4637
      </li>
      <li>
        <svg viewBox="0 0 10 10" aria-hidden="true"><g fill="none" stroke="var(--graphite)" stroke-width="0.9"><circle cx="5" cy="5" r="4.2"/><ellipse cx="5" cy="5" rx="1.8" ry="4.2"/><line x1="0.8" y1="5" x2="9.2" y2="5"/></g></svg>
        www.bramblefordwinecellar.com.au
      </li>
      <li>
        <svg viewBox="0 0 10 10" aria-hidden="true"><rect x="1" y="2" width="8" height="6" fill="var(--wine)"/><path d="M1 2 L5 5.5 L9 2" fill="none" stroke="#fff" stroke-width="0.8"/></svg>
        bramblefordwinecellar@mailvista.com
      </li>
    </ul>
    <div class="back-mark">
      <span class="mark-dot" aria-hidden="true"></span>
      <p>Brambleford<br>Wine Cellar</p>
    </div>
  </section>

  <section class="card card-front" aria-label="Card front with brand">
    <h1 class="brand-name">Brambleford<small>Wine Cellar</small></h1>
    <div class="social-row" aria-label="Social media links">
      <span></span><span></span><span></span><span></span>
    </div>
    <div class="emblem" role="img" aria-label="Brand emblem area, embossed grey and wine red"></div>
    <p class="emblem-caption">Independent Wine Shop</p>
  </section>
</main>
</body>
</html>
```